Vegan Jerky company needs a label for it's pouch, and a new logo

Dear Designers - this used to be a guaranteed project, however, due to the low quality of designs I have received, I have removed the guaranteed status. However, we need this product made and we will pay for a great, high quality design that meets the requirements of our brief.

We need sticker labels that will go onto the front and back of our vegan jerky package. Our package is a zip-sealable pouch, and we will either go with black, white or brown for the color of the pouch.

We need the concept, artwork, theme and logo designed. Pls choose the colors.

There will be four flavors. These can be finished as part of another project. The flavors are: Smoked Maple, Cracked Pepper, Teriyaki Sriracha, Original.

We are Lonny and Marva's Vegan Jerky.

Our food is vegan, non GMO, straight from the farm, organic, healthy, pure, clean, made in small batches and earth friendly. We use no chemicals or artificial flavors and our product is 100% natural.

Our kitchen is yours.
Updates

Low designer entries

Target Market(s)

Vegetarians, vegans, health conscious, ecological, intelligent, caring.

Industry/Entity Type

Food Production

Logo Text

"Lonny and Marva" and "Our Kitchen is Yours"

Colors

Designer to choose colors to be used in the design.

Requirements
Must have
• earth friendly design, classy, hipster, vegan design, shabby chic,
Nice to have
• i have no ideas really...
• We prefer black and while, with a little splash of color. The last file is an idea I had but please use your own vision.

```html
<!DOCTYPE html>
<html lang="en">
<head>
<meta charset="utf-8">
<title>Lonny and Marva's Vegan Jerky – Pouch Labels</title>
<link rel="stylesheet" href="https://fonts.googleapis.com/css2?family=Amatic+SC:wght@400;700&family=Caveat:wght@600&family=Patrick+Hand&display=swap">
<style>
  :root {
    --backdrop: #f4f1ec;
    --label-white: #ffffff;
    --ink: #2b2b2b;
    --rule: #3a3a3a;
    --teriyaki: #e6a72a;
    --teriyaki-soft: #fbefd3;
    --original: #3a3a3a;
    --original-soft: #ececec;
    --maple: #7da74a;
    --maple-soft: #e7f0dc;
  }
  * { box-sizing: border-box; margin: 0; padding: 0; }
  html, body {
    width: 917px;
    height: 1200px;
    overflow: hidden;
    background: var(--backdrop);
  }
  .canvas {
    position: relative;
    width: 917px;
    height: 1200px;
  }
  .label {
    position: absolute;
    width: 340px;
    height: 480px;
    background: var(--label-white);
    box-shadow: 0 2px 10px rgba(0,0,0,0.08);
    overflow: hidden;
  }
  .label--teriyaki { left: 55px; top: 105px; --accent: var(--teriyaki); --accent-soft: var(--teriyaki-soft); }
  .label--original { left: 515px; top: 105px; --accent: var(--original); --accent-soft: var(--original-soft); }
  .label--maple { left: 288px; top: 690px; --accent: var(--maple); --accent-soft: var(--maple-soft); }

  .label__pattern {
    position: absolute;
    inset: 0;
    background:
      radial-gradient(ellipse at 15% 10%, var(--accent-soft) 0%, transparent 55%),
      radial-gradient(ellipse at 90% 95%, var(--accent-soft) 0%, transparent 55%),
      radial-gradient(ellipse at 85% 20%, var(--accent-soft) 0%, transparent 40%),
      var(--label-white);
  }
  .label__content {
    position: relative;
    display: flex;
    flex-direction: column;
    align-items: center;
    height: 100%;
    padding-top: 68px;
  }
  .brand-seal {
    width: 184px;
    height: 184px;
    border-radius: 50%;
    background: var(--accent);
    display: flex;
    align-items: center;
    justify-content: center;
    text-align: center;
    padding: 20px;
  }
  .brand-seal__name {
    font-family: "Amatic SC", cursive;
    font-weight: 700;
    font-size: 34px;
    line-height: 1;
    color: var(--label-white);
  }
  .flavor {
    display: flex;
    align-items: center;
    gap: 10px;
    width: 268px;
    margin-top: 40px;
  }
  .flavor::before, .flavor::after {
    content: "";
    flex: 1;
    height: 2px;
    background: var(--rule);
  }
  .flavor__name {
    font-family: "Amatic SC", cursive;
    font-weight: 700;
    font-size: 26px;
    letter-spacing: 1px;
    color: var(--accent);
    white-space: nowrap;
  }
  .label--original .flavor__name { letter-spacing: 4px; }
  .claim {
    font-family: "Caveat", cursive;
    font-weight: 600;
    font-size: 22px;
    color: var(--ink);
    margin-top: 6px;
  }
  .badges {
    display: flex;
    border: 2px solid var(--ink);
    margin-top: 8px;
  }
  .badges__item {
    font-family: "Patrick Hand", cursive;
    font-size: 15px;
    color: var(--ink);
    padding: 2px 14px;
    background: var(--label-white);
  }
  .badges__item + .badges__item { border-left: 2px solid var(--ink); }
</style>
</head>
<body>
<main class="canvas">

  <article class="label label--teriyaki">
    <div class="label__pattern" role="img" aria-label="Light geometric network of fine lines and dots in amber"></div>
    <div class="label__content">
      <div class="brand-seal"><span class="brand-seal__name">Lonny and Marva's Vegan Jerky</span></div>
      <h2 class="flavor"><span class="flavor__name">Teriyaki Sriracha</span></h2>
      <p class="claim">100% Natural Vegan</p>
      <div class="badges"><span class="badges__item">Non GMO</span><span class="badges__item">Organic</span></div>
    </div>
  </article>

  <article class="label label--original">
    <div class="label__pattern" role="img" aria-label="Light geometric network of fine lines and dots in charcoal"></div>
    <div class="label__content">
      <div class="brand-seal"><span class="brand-seal__name">Lonny and Marva's Vegan Jerky</span></div>
      <h2 class="flavor"><span class="flavor__name">Original</span></h2>
      <p class="claim">100% Natural Vegan</p>
      <div class="badges"><span class="badges__item">Non GMO</span><span class="badges__item">Organic</span></div>
    </div>
  </article>

  <article class="label label--maple">
    <div class="label__pattern" role="img" aria-label="Light geometric network of fine lines and dots in leaf green"></div>
    <div class="label__content">
      <div class="brand-seal"><span class="brand-seal__name">Lonny and Marva's Vegan Jerky</span></div>
      <h2 class="flavor"><span class="flavor__name">Smoked Maple</span></h2>
      <p class="claim">100% Natural Vegan</p>
      <div class="badges"><span class="badges__item">Non GMO</span><span class="badges__item">Organic</span></div>
    </div>
  </article>

</main>
</body>
</html>
```